Accountant website

Please design a accountant website for www.fenwaylodgeadvisory.com.au. This site is majorly out of date, and is not supported by modern browsers.

The style should use the reds from the design at dev.fenwaylodgeadvisory.com.au, and should be modern and make use of Slides (large content slides that the user scrolls through on the front page).

The content is largely already on the site, however happy to move some around to suit the modern design as required.

The dev.fenwaylodgeadvisory.com.au was a rough mock up that I have completed that the client is "happy" with the direction, however this needs a lot of polish and finishing touches, and I will accept designs that differ from this, but highly recommend that this is used as a guide.

Ready to be sliced PSD Only - HTML no required.

In all honesty, although I can technically do a lot of this, the polished finished I want for this site has eluded me in a few attempts, and therefore I am looking out there at you much more artistic people to finish (or redesign if required) this site.

Target Market(s)

Higher end Small - Medium Business

Industry/Entity Type

Accountant

Requirements
Must have
• Must use the logo from dev.fenwaylodgeadvisory.com.au use exactly the red colours as defined in this layout. A basic layout PSD (to get the colour etc) and the logo in ai format is attached to this project. Please ignore the SSL warning on the development site.

The final product does NOT have to be the same as shown on dev.fenwaylodgeadvisory.com.au however the red colour scheme must be used. The client DOES want the logo on the RIGHT.

Must have a front landing page design, and a page layout that considers the other page content (at least one separate PSD)
Nice to have
• I really am looking at a slide format for the front page simular to:

http://www.plumvine.com/au/
http://www.tidelockbox.com/

The attached photos should be used on the site. Was considering a rotating banner with these images are a watermark background on a solid Red header bar, but happy to be shown other options.
Should not have
• Please no "Pattern Goblin" submissions.

```html
<!DOCTYPE html>
<html lang="en">
<head>
<meta charset="utf-8">
<title>Working With Us – Fenway Lodge Advisory</title>
<link href="https://fonts.googleapis.com/css2?family=Roboto+Condensed:wght@300;400;700&family=Roboto:wght@400;500&display=swap" rel="stylesheet">
<style>
:root{
  --red:#c1272d;
  --red-dark:#9e1b20;
  --ink:#2b2b2b;
  --body:#4a4a4a;
  --muted:#9a9a9a;
  --page:#f4f4f4;
  --card:#ffffff;
  --rule:#dcdcdc;
  --footer:#1e1e1e;
  --footer-text:#cfcfcf;
}
*{box-sizing:border-box;margin:0;padding:0}
html,body{width:1200px;height:2381px;overflow:hidden}
body{background:var(--page);font-family:"Roboto",Arial,sans-serif;color:var(--body);position:relative}
.head{font-family:"Roboto Condensed",Arial,sans-serif}
.abs{position:absolute}

/* header */
.site-header{position:absolute;left:0;top:0;width:1200px;height:107px;background:#fff}
.util-links{position:absolute;left:183px;top:11px;display:flex;gap:20px;font-size:11px;color:#555}
.util-links span{display:flex;align-items:center;gap:5px}
.util-links i{width:10px;height:10px;background:#777;border-radius:2px;display:inline-block}
.main-nav{position:absolute;left:183px;top:54px;display:flex;gap:6px;font-size:15px;color:#333}
.main-nav a{padding:6px 10px;color:inherit;text-decoration:none}
.main-nav a.active{background:var(--red);color:#fff}
.brand{position:absolute;left:822px;top:18px;display:flex;align-items:center;gap:12px}
.brand-name{font-family:"Roboto Condensed",Arial,sans-serif;font-weight:700;font-size:30px;color:#222;line-height:1;letter-spacing:.5px}
.brand-mark{width:34px;height:34px;background:var(--red)}

/* banner */
.page-banner{position:absolute;left:0;top:107px;width:1200px;height:222px;background:linear-gradient(90deg,#3d4a2e 0%,#6b6a4a 40%,#a39a7a 65%,#6d7a3e 100%)}
.banner-title{position:absolute;left:179px;top:62px;color:#fff;font-family:"Roboto Condensed",Arial,sans-serif;font-weight:700;font-size:44px;line-height:1}
.banner-sub{position:absolute;left:179px;top:110px;color:#f1f1f1;font-family:"Roboto Condensed",Arial,sans-serif;font-weight:300;font-size:27px;line-height:32px}

/* principal */
.principal{position:absolute;left:179px;top:378px;width:846px}
.principal h1{color:var(--red);font-family:"Roboto Condensed",Arial,sans-serif;font-weight:400;font-size:32px;margin-bottom:14px}
.principal p{font-size:14px;line-height:19px;color:#444;margin-bottom:14px}

/* team intro */
.team-intro{position:absolute;left:179px;top:614px;width:842px;height:238px;background:var(--card)}
.team-photo{position:absolute;left:0;top:0;width:274px;height:238px;background:linear-gradient(90deg,#7a6a55,#c9b39a 60%,#fff)}
.team-intro h2{position:absolute;left:324px;top:36px;color:var(--red);font-family:"Roboto Condensed",Arial,sans-serif;font-weight:400;font-size:32px}
.team-intro p{position:absolute;left:324px;top:86px;width:490px;font-size:16px;line-height:23px;color:var(--muted)}

.meet-title{position:absolute;left:0;width:1200px;top:888px;text-align:center;font-family:"Roboto Condensed",Arial,sans-serif;font-weight:300;font-size:56px;color:#d4d4d4;letter-spacing:1px}

/* team cards */
.team-card{position:absolute;top:981px;width:258px;height:371px;background:var(--card);text-align:center}
.team-card .portrait{height:160px;background:linear-gradient(180deg,#8fa6bb 0%,#c7d3dc 60%,#fff 100%)}
.team-card h3{margin-top:62px;color:var(--red);font-family:"Roboto Condensed",Arial,sans-serif;font-weight:700;font-size:17px}
.team-card p{margin:12px auto 0;width:214px;font-size:11.5px;line-height:17px;color:#444}

.divider{position:absolute;left:179px;width:845px;height:1px;background:var(--rule)}

/* services */
.service{position:absolute;width:402px}
.service h2{font-family:"Roboto Condensed",Arial,sans-serif;font-weight:700;font-size:20px;color:var(--ink);margin-bottom:18px}
.service .pic{float:left;width:190px;height:146px;margin:0 14px 4px 0}
.service p{font-size:13.5px;line-height:23.5px;color:#444;text-align:justify}

/* footer */
.footer-line{position:absolute;left:0;top:2165px;width:1200px;height:5px;background:var(--red)}
.site-footer{position:absolute;left:0;top:2170px;width:1200px;height:211px;background:var(--footer);color:var(--footer-text)}
.site-footer h4{font-family:"Roboto Condensed",Arial,sans-serif;font-weight:700;font-size:18px;color:#fff}
.sitemap{position:absolute;left:179px;top:40px}
.sitemap-cols{display:flex;gap:34px;margin-top:20px}
.sitemap ul{list-style:none;font-size:11px;line-height:15px}
.sitemap li::before{content:"";display:inline-block;width:4px;height:4px;background:var(--red);margin-right:7px;vertical-align:middle}
.map{position:absolute;left:424px;top:44px;width:183px;height:119px;background:linear-gradient(135deg,#e6e2d6,#cfd9c4 55%,#b9cfe0)}
.contact{position:absolute;left:631px;top:40px}
.contact .addr{font-size:10.5px;line-height:14px;margin:22px 0 8px 18px}
.contact .tel{display:flex;align-items:center;gap:7px;font-size:11px;margin-bottom:5px;color:#fff}
.badge-box{position:absolute;left:798px;top:44px;width:221px;height:64px;background:#fff;display:flex;align-items:center;justify-content:center;gap:14px}
.badge-box .seal{width:36px;height:36px;border-radius:50%;background:var(--red)}
.badge-box .tag{width:120px;height:14px;background:#cfcfcf}
.copyright{position:absolute;left:798px;top:124px;font-size:10.5px;line-height:14px}
</style>
</head>
<body>

<header class="site-header">
  <div class="util-links"><span><i></i>Login</span><span><i></i>Register</span><span><i></i>Contact Us</span><span><i></i>Testimonials</span></div>
  <nav class="main-nav">
    <a>About Us</a><a>Services</a><a class="active">Working With Us</a><a>Testimonials</a><a>Article Of The Moment</a>
  </nav>
  <div class="brand"><span class="brand-name">FENWAY LODGE</span><span class="brand-mark"></span></div>
</header>

<section class="page-banner" role="img" aria-label="Photograph of the four team members standing outdoors against greenery">
  <div class="banner-title">WORKING WITH US</div>
  <div class="banner-sub">But we make detailed analysis of<br>your finance easy</div>
</section>

<section class="principal">
  <h1>The Principal – Helena Marsh</h1>
  <p>Helena achieved her Bachelor of Commerce degree from the University of Eastbrook in 2001 and went on to complete her Certified Ledger Accountant qualifications. She has been a member of the Institute of Certified Ledger Accountants since May 2005.</p>
  <p>With over 11 years experience in the accounting profession, working with high profile businesses within the Eastbrook area, Helena has developed a great understanding of the varying needs of different businesses within their industries. Helena established Fenway Lodge Advisory in 2006 from a desire to offer small business clients a more personalised service. Her aim is to work with business owners on improving their business systems and performance.</p>
</section>

<section class="team-intro">
  <div class="team-photo" role="img" aria-label="Portrait photograph of the principal"></div>
  <h2>The Team</h2>
  <p>Helena is supported by a team of 3 staff who understand the importance of developing and maintaining client relationships.The team are dedicated to providing you with the best possible service which exceeds your expectations.</p>
</section>

<div class="meet-title">MEET THE TEAM</div>

<article class="team-card" style="left:179px">
  <div class="portrait" role="img" aria-label="Portrait photograph of Tessa Whitford by the harbour"></div>
  <h3>TESSA WHITFORD</h3>
  <p>Tessa commenced with Fenway Lodge Advisory in September 2008. Tessa performs bookkeeping work on behalf of clients and manages the office accounts.</p>
</article>
<article class="team-card" style="left:469px">
  <div class="portrait" role="img" aria-label="Portrait photograph of Corinne Dale by the harbour"></div>
  <h3>CORINNE DALE</h3>
  <p>Corinne joined the Fenway Lodge Advisory team in January 2009. Corinne has completed her Bachelor of Commerce Degree, and has commenced her studies to become a Certified Accountant.</p>
</article>
<article class="team-card" style="left:762px">
  <div class="portrait" role="img" aria-label="Portrait photograph of Lydia Overton by the harbour"></div>
  <h3>LYDIA OVERTON</h3>
  <p>The newest member to our team, Lydia is undertaking a trainee administration role. Lydia's primary duties include managing client relations and receptional functions.</p>
</article>

<div class="divider" style="top:1405px"></div>

<section class="service" style="left:179px;top:1440px">
  <h2>Complimentary Client Consultation</h2>
  <div class="pic" role="img" aria-label="Photograph of a business meeting around a desk" style="background:linear-gradient(135deg,#d8d8d8,#8a8f98 60%,#4a4d55)"></div>
  <p>A one-hour meeting is held at a mutually convenient time to enable us to learn about you and your business. Throughout which the focus is on your business. We discuss the challenges you face in your business, and brainstorm how we can assist you with overcoming these challenges. We also discuss your goals and the future direction you want your business to take.</p>
</section>

<section class="service" style="left:624px;top:1440px">
  <h2>Ongoing Business Advice</h2>
  <div class="pic" role="img" aria-label="Photograph of a pen over a financial chart" style="background:linear-gradient(135deg,#f2f2f5,#b9c3d8 60%,#7d8fb8)"></div>
  <p>Depending on the service agreement, regular monthly or quarterly meetings are conducted to perform the services agreed upon during the previous stage. These services may include: the review of business performance, industry analysis, budget preparation, cash flow analysis, or the establishment setting and measurement of the achievement of business goals.</p>
</section>

<div class="divider" style="top:1745px"></div>

<section class="service" style="left:179px;top:1775px">
  <h2>Quote Acceptance</h2>
  <div class="pic" role="img" aria-label="Photograph of a coffee cup on a newspaper" style="background:linear-gradient(135deg,#f3f3f3,#c9c9c9 55%,#6e6e6e)"></div>
  <p>Once the final annual fee is established, a supply agreement is issued for client review and signature. Fenway Lodge Advisory then handles all correspondence with the existing accountant, if applicable, to ensure that there is no professional objection in the appointment of Fenway Lodge Advisory as your new business adviser. Once confirmation of this is received, Fenway Lodge Advisory is appointed as the registered agent with the National Revenue Office, and Corporate Registry Commission.</p>
</section>

<section class="service" style="left:624px;top:1775px">
  <h2>Customised Accounting Solution</h2>
  <div class="pic" role="img" aria-label="Photograph of a businessman seated at a chessboard" style="background:linear-gradient(135deg,#4a4a4a,#1c1c1c 60%,#6a6a6a)"></div>
  <p>After considering the items raised in the initial consult, Fenway Lodge Advisory then develops a customised proposal to meet the needs of your business. Each service contained in the quote has been specifically selected to achieve a desired outcome. A second meeting is then held to discuss the proposal and ensure both parties are satisfied. If necessary, modifications are made to the proposal to enable a final annual fee to be determined and agreed upon.</p>
</section>

<div class="footer-line"></div>
<footer class="site-footer">
  <div class="sitemap">
    <h4>Site Map</h4>
    <div class="sitemap-cols">
      <ul><li>About us</li><li>Services</li><li>Working with us</li><li>Contact us</li><li>Testimonials</li></ul>
      <ul><li>News</li><li>NewsRSS</li><li>Article Of The</li><li>Moment Archive</li><li>Client Login</li></ul>
    </div>
  </div>
  <div class="map" role="img" aria-label="Street map showing the office location"></div>
  <div class="contact">
    <h4>Contact Us</h4>
    <div class="addr">14/27 Corran St<br>ASHBY NSW 2290</div>
    <div class="tel"><svg width="11" height="11" viewBox="0 0 12 12"><path d="M3 1l2 2-1 2c1 1.5 2 2.5 3 3l2-1 2 2-1.5 2C5 11 1 7 1 2.5z" fill="#c1272d"/></svg>02 4000 1100</div>
    <div class="tel"><svg width="11" height="11" viewBox="0 0 12 12"><path d="M3 1l2 2-1 2c1 1.5 2 2.5 3 3l2-1 2 2-1.5 2C5 11 1 7 1 2.5z" fill="#c1272d"/></svg>02 4000 1199</div>
  </div>
  <div class="badge-box"><span class="seal"></span><span class="tag"></span></div>
  <div class="copyright">Copyright © 2013 Fenway Lodge Advisory<br>All rights reserved</div>
</footer>

</body>
</html>
```